Marbol Gardens Business Card Design

My company is about Natural products made from Bees Wax, of which I am farming/raising. Products like Honey when in season, body butter, hand cream, lotions, lip balm, soap and more! All Natural, with Beeswax as the base, as it has large healing properties for moisturizing and nourishing your skin.
I would prefer lots of yellows, browns, and blacks (but am open)! I think black ink on the artwork may show up the best. But your the professionals!
The artwork is very dear to me, as my son, Warren did this in the hospital when he was diagnosed with Leukemia, of which he did not survive, at eighteen.
Is it possible to put his initials on this? WJT in light colored ink.
FROM HIVE TO HAND Oops! I need my name on there. Paula Dimmick and number 555-014-2297. Thank you all so much.

Hospital

Marbol Gardens
All Natural Products
Paula Dimmick
555-014-2297
MarbolGardens@plimmet.com

```html
<!DOCTYPE html>
<html lang="en">
<head>
<meta charset="utf-8">
<title>Marbol Gardens Business Card</title>
<link rel="stylesheet" href="https://fonts.googleapis.com/css2?family=Marcellus+SC&family=Cinzel:wght@400;600&display=swap">
<style>
  :root {
    --backdrop: #e8e2d6;
    --card-white: #ffffff;
    --card-cream: #fcfae6;
    --honey: #e9cf3a;
    --honey-soft: #f6eeb0;
    --comb-tone: #f3edc9;
    --band-yellow: #f7ea12;
    --ink: #1c1c1c;
    --name-gold: #8f7a2a;
    --rule: #9a9a9a;
  }
  * { box-sizing: border-box; margin: 0; padding: 0; }
  html, body { width: 1200px; height: 714px; overflow: hidden; }
  body {
    background: var(--backdrop);
    font-family: "Marcellus SC", "Cinzel", serif;
    position: relative;
  }
  .card {
    position: absolute;
    top: 205px;
    width: 530px;
    height: 303px;
    overflow: hidden;
    box-shadow: 0 2px 6px rgba(0,0,0,.18);
  }
  .card--front { left: 50px; background: var(--card-white); }
  .card--back { left: 620px; background: var(--card-cream); }

  .brand {
    position: absolute;
    display: flex;
    flex-direction: column;
    align-items: center;
  }
  .brand__row { display: flex; align-items: center; gap: 8px; }
  .brand__dot { border-radius: 50%; background: var(--honey); }
  .brand__name {
    font-family: "Marcellus SC", serif;
    color: var(--honey);
    white-space: nowrap;
  }
  .brand__tagline {
    font-family: "Cinzel", serif;
    font-weight: 600;
    color: var(--honey);
    letter-spacing: .5px;
    white-space: nowrap;
  }

  .card--front .brand { left: 110px; top: 42px; width: 240px; }
  .card--front .brand__dot { width: 22px; height: 22px; }
  .card--front .brand__name { font-size: 24px; }
  .card--front .brand__tagline { font-size: 9px; margin-top: 8px; }

  .holder {
    position: absolute;
    left: 70px;
    top: 193px;
  }
  .holder__name {
    font-size: 21px;
    color: var(--name-gold);
    letter-spacing: .5px;
    white-space: nowrap;
  }
  .holder__role {
    font-size: 14px;
    color: var(--ink);
    margin-top: 2px;
    padding-left: 56px;
  }
  .divider {
    position: absolute;
    left: 258px;
    top: 150px;
    width: 1px;
    height: 100px;
    background: var(--rule);
  }
  .contacts {
    position: absolute;
    left: 270px;
    top: 150px;
    list-style: none;
    font-family: "Cinzel", serif;
    font-size: 12px;
    color: var(--ink);
    line-height: 18px;
    white-space: nowrap;
  }
  .contacts li { display: flex; align-items: center; gap: 7px; }
  .contacts__mark {
    width: 9px; height: 9px; border-radius: 50%;
    background: var(--ink); flex: none;
  }
  .bands { position: absolute; left: 0; bottom: 0; }

  .honeycomb {
    position: absolute;
    inset: 0;
    background: radial-gradient(ellipse at 50% 45%, var(--honey-soft) 0%, var(--comb-tone) 40%, var(--card-cream) 75%);
  }
  .card--back .brand { left: 0; right: 0; top: 108px; }
  .card--back .brand__dot { width: 34px; height: 34px; }
  .card--back .brand__name { font-size: 40px; }
  .card--back .brand__tagline { font-size: 14px; margin-top: 16px; }
</style>
</head>
<body>
  <section class="card card--front">
    <div class="brand">
      <div class="brand__row">
        <span class="brand__dot"></span>
        <span class="brand__name">Marbol Gardens</span>
      </div>
      <span class="brand__tagline">FROM HIVE TO HAND</span>
    </div>

    <div class="holder">
      <p class="holder__name">Paula Dimmick</p>
      <p class="holder__role">Consultant</p>
    </div>

    <span class="divider"></span>

    <ul class="contacts">
      <li><span class="contacts__mark"></span>555-014-2297</li>
      <li><span class="contacts__mark"></span>555-014-7731</li>
      <li><span class="contacts__mark"></span>MARBOLGARDENS@PLIMMET.COM</li>
      <li><span class="contacts__mark"></span>WWW.MARBOLGARDENS.NET</li>
    </ul>

    <svg class="bands" width="530" height="60" viewBox="0 0 530 60" aria-hidden="true">
      <polygon points="0,60 0,44 200,22 185,60" fill="var(--ink)"/>
      <polygon points="212,60 232,34 530,6 530,60" fill="var(--band-yellow)"/>
      <polygon points="232,60 246,44 530,22 530,60" fill="var(--card-white)"/>
    </svg>
  </section>

  <section class="card card--back">
    <div class="honeycomb" role="img" aria-label="Faint pale-yellow honeycomb pattern spread across the card"></div>
    <div class="brand">
      <div class="brand__row">
        <span class="brand__dot"></span>
        <span class="brand__name">Marbol Gardens</span>
      </div>
      <span class="brand__tagline">FROM HIVE TO HAND</span>
    </div>
  </section>
</body>
</html>
```